Design a Mobile First Website for a Salad Resturant

** WEBSITE LIKE AN APP, NOT LANDING PAGE **

1. Homepage
Objective: Introduce the brand and direct visitors to either start creating their custom salad or explore the menu of pre-designed salads.
Design Elements:
Clean and minimalistic layout with high-quality images of fresh salads.
Two prominent buttons: "Create Your Salad" and "Our Salads".
Brief welcome message that highlights the freshness and quality of ingredients.

2. Create Your Salad Page
Objective: Allow customers to design their salad from a list of ingredients.
Design Elements:
Interactive, step-by-step builder interface where customers can select ingredients. Each ingredient category (like greens, proteins, toppings, dressings) should be a separate step in the process.
Visual representation of their salad being built as they select ingredients.
Information icons next to each ingredient for dietary information (e.g., vegan, gluten-free, calories).
Option to save favorite combinations or reorder past salads.
Clear price updates as they add or remove ingredients.

3. Our Salads Page
Objective: Showcase a list of pre-designed salad options that customers can quickly choose from.
Design Elements:
Grid layout with images and brief descriptions of each pre-designed salad.
Include customer reviews and ratings for each salad.
Easy "Add to Cart" option from this page.

4. Cart and Checkout Page
Objective: Streamline the checkout process with minimal steps.
Design Elements:
Summary of order with options to modify quantities or remove items.
Simple form for entering delivery details, with the ability to remember details for returning customers.
Secure payment gateway integration.
A confirmation screen with estimated delivery time and order tracking capabilities.

5. Mobile Optimization
Approach: Since this is a "Mobile First Design", ensure that:
The website is responsive and elements like buttons, text, and images scale properly across different devices.
Touch-friendly interfaces with large tap targets for ease of use on mobile devices.
Fast loading times by optimizing images and using mobile-first coding practices.

Target Market(s)

Food

Industry/Entity Type

Food

Number of Pages Required

4 page

Requirements
Must have
• Modren Design, Mobile First

```html
<!DOCTYPE html>
<html lang="en">
<head>
<meta charset="utf-8">
<title>Greenbowl – Salad Ordering Screens</title>
<link href="https://fonts.googleapis.com/css2?family=Karla:wght@400;600;700;800&family=Lexend:wght@300;400;500&family=Inter:wght@600&display=swap" rel="stylesheet">
<style>
:root{
  --bg:#fdd07e;
  --olive:#a6b47f;
  --olive-deep:#8f9c63;
  --olive-text:#9ea86a;
  --navy:#3d4868;
  --lavender:#8e88c6;
  --orange:#e07b4f;
  --peach:#e6a867;
  --ink:#2f2f33;
  --muted:#a9a9ad;
  --line:#e3e3e6;
  --panel:#f1f1f3;
  --white:#ffffff;
}
*{box-sizing:border-box;margin:0;padding:0}
html,body{width:813px;height:1200px;overflow:hidden;background:var(--bg)}
.stage{position:relative;width:1574px;height:2324px;transform:scale(.5165);transform-origin:0 0;background:var(--bg);font-family:"Lexend",sans-serif;color:var(--ink)}
.screen{position:absolute;width:231px;background:var(--white);border-radius:26px;overflow:hidden}
.screen.green{background:var(--olive)}
.status{position:absolute;top:0;left:0;width:231px;height:34px}
.status .time{position:absolute;left:26px;top:9px;font:600 10px "Inter",sans-serif}
.green .status .time{color:#fff}
.status .island{position:absolute;left:78px;top:5px;width:75px;height:22px;border-radius:11px;background:#000}
.status svg{position:absolute;right:18px;top:11px}
.home-bar{position:absolute;bottom:8px;left:77px;width:77px;height:3px;border-radius:2px;background:#222}
.photo{position:absolute;border-radius:8px}
.page-title{position:absolute;right:12px;top:48px;font:800 15px "Karla",sans-serif;color:var(--olive-text);letter-spacing:.2px}
.back{position:absolute;left:12px;top:48px;width:16px;height:16px}
.tiny{font-size:4px;line-height:5.5px;color:var(--muted)}

/* splash */
.brand{position:absolute;left:0;width:231px;text-align:center;font:800 34px "Karla",sans-serif;color:var(--navy)}
.quote{position:absolute;left:0;width:231px;text-align:center;font:300 12.5px/16px "Lexend",sans-serif;color:#fff}

/* home */
.welcome{position:absolute;left:12px;top:48px;font:300 8px "Lexend",sans-serif;color:var(--muted)}
.user{position:absolute;left:12px;top:62px;font:400 9px "Lexend",sans-serif}
.avatar{position:absolute;border-radius:50%}
.section-title{position:absolute;left:12px;font:700 9.5px "Karla",sans-serif;color:var(--olive-text)}
.section-copy{position:absolute;left:12px;width:95px}
.pill{position:absolute;left:12px;width:46px;height:14px;border-radius:3px;background:var(--olive);color:#fff;font:400 4.5px/14px "Lexend",sans-serif;text-align:center}
.label{position:absolute;left:12px;font:300 8px "Lexend",sans-serif;color:var(--muted)}
.rating{position:absolute;left:12px;font:400 5px "Lexend",sans-serif;color:var(--peach)}
.price-tag{position:absolute;right:12px;font:400 6px "Lexend",sans-serif;color:var(--muted)}
.mini-card{position:absolute;left:11px;width:209px;height:58px;border-radius:6px;box-shadow:0 2px 4px rgba(0,0,0,.12)}
.mini-card .bowl{position:absolute;top:5px;width:54px;height:48px;border-radius:50%}
.mini-card .kcal{position:absolute;font:300 5px "Lexend",sans-serif;color:var(--muted)}
.mini-card .name{position:absolute;font:700 10px "Karla",sans-serif;white-space:nowrap}
.mini-card .meta{position:absolute;font:300 4.5px "Lexend",sans-serif;color:var(--muted)}

/* builder */
.qty{position:absolute;display:flex;align-items:center;gap:4px}
.qty .btn{width:11px;height:11px;border-radius:50%;background:var(--orange);color:#fff;font:700 9px/11px "Karla",sans-serif;text-align:center}
.qty .val{width:20px;height:11px;border:1px solid var(--orange);border-radius:2px;font:400 6.5px/9px "Lexend",sans-serif;text-align:center}
.total{position:absolute;right:12px;top:178px;font:300 10px "Lexend",sans-serif;color:#555}
.divider-band{position:absolute;left:0;top:200px;width:231px;height:6px;background:var(--panel)}
.step{position:absolute;left:12px;font:400 8px "Lexend",sans-serif;color:var(--olive-text);display:flex;align-items:center;gap:4px}
.step i{width:9px;height:9px;border:1px solid var(--olive-text);border-radius:50%;font:400 5px/7px "Lexend",sans-serif;font-style:normal;text-align:center}
.ing{position:absolute;width:47px;height:55px;border-radius:4px;background:#fff;box-shadow:0 1px 3px rgba(0,0,0,.18)}
.ing.sel{background:var(--olive)}
.ing .ing-img{position:absolute;top:-18px;left:6px;width:35px;height:30px;border-radius:50%}
.ing .ing-name{position:absolute;top:17px;left:0;width:47px;text-align:center;font:400 4px "Lexend",sans-serif;color:#555;white-space:nowrap}
.ing.sel .ing-name,.ing.sel li{color:#fff}
.ing ul{position:absolute;top:25px;left:4px;list-style:none}
.ing li{font:300 3.6px/5px "Lexend",sans-serif;color:var(--muted)}
.ing li::before{content:"";display:inline-block;width:3px;height:3px;border-radius:50%;background:#222;margin-right:2px;vertical-align:middle}
.ing .ing-price{position:absolute;bottom:-16px;left:18px;width:11px;height:11px;border-radius:50%;background:var(--olive);color:#fff;font:400 4px/11px "Lexend",sans-serif;text-align:center}
.cta{position:absolute;left:12px;width:207px;height:23px;border-radius:4px;background:var(--orange);color:#fff;font:700 9px/23px "Karla",sans-serif;text-align:center}

/* menu */
.dish{position:absolute;left:11px;width:209px;height:138px;border-radius:6px;box-shadow:0 2px 5px rgba(0,0,0,.15)}
.dish .bowl{position:absolute;left:6px;top:5px;width:60px;height:52px;border-radius:50%}
.dish .kcal{position:absolute;left:95px;top:12px;font:300 5px "Lexend",sans-serif;color:var(--muted)}
.dish .cost{position:absolute;right:12px;top:10px;font:400 6px "Lexend",sans-serif;color:var(--muted)}
.dish .name{position:absolute;left:95px;top:21px;font:700 10.5px "Karla",sans-serif;white-space:nowrap}
.dish .meta{position:absolute;left:95px;top:37px;font:300 4.5px "Lexend",sans-serif;color:var(--muted)}
.dish .desc{position:absolute;left:12px;top:66px;width:188px}
.dish .rev-face{position:absolute;left:12px;top:99px;width:20px;height:20px;border-radius:50%}
.dish .rev{position:absolute;left:42px;top:101px;width:80px;font:300 4.2px/5.5px "Lexend",sans-serif;color:#555}
.dish .stars{position:absolute;left:42px;top:120px;font:400 5px "Lexend",sans-serif;color:var(--peach);letter-spacing:.5px}
.dish .who{position:absolute;left:96px;top:122px;font:400 4.5px "Lexend",sans-serif;color:#555}
.dish .add{position:absolute;right:9px;top:108px;width:48px;height:14px;border-radius:3px;color:#fff;font:400 4.5px/14px "Lexend",sans-serif;text-align:center}

/* order */
.line-item{position:absolute;left:11px;width:209px;height:56px;border-radius:6px;background:#fff;box-shadow:0 2px 5px rgba(0,0,0,.15)}
.line-item .bowl{position:absolute;left:8px;top:4px;width:52px;height:48px;border-radius:50%}
.line-item .name{position:absolute;left:84px;top:13px;font:700 10px "Karla",sans-serif;color:var(--olive-text);white-space:nowrap}
.line-item .each{position:absolute;left:84px;top:30px;font:400 10px "Lexend",sans-serif;color:var(--olive-text)}
.line-item .each small{font-size:5px;color:var(--muted)}
.line-item .qty{right:10px;top:33px}
.line-item .remove{position:absolute;right:6px;top:5px;width:8px;height:8px;border-radius:50%;background:#c9c9cc;color:#fff;font:700 6px/8px "Karla",sans-serif;text-align:center}
.field{position:absolute;height:22px;border:1px solid #d9d9dc;border-radius:4px;background:#fff;padding-left:7px;font:300 6px/20px "Lexend",sans-serif;color:var(--muted)}
.sum{position:absolute;left:11px;width:209px;display:flex;justify-content:space-between;font:300 9px "Lexend",sans-serif;color:var(--muted)}
.sum.strong{color:var(--olive-text);font-weight:400}
.pay-panel{position:absolute;left:0;top:408px;width:231px;height:303px;background:var(--panel)}
.pay-title{position:absolute;left:0;top:20px;width:231px;text-align:center;font:300 9px "Lexend",sans-serif;color:#555}
.bank-card{position:absolute;left:11px;top:42px;width:209px;height:130px;border-radius:3px;background:linear-gradient(125deg,#5a3ea2 0%,#9b3579 55%,#d9484d 100%);color:#fff}
.bank-card .type{position:absolute;left:16px;top:10px;font:500 6px "Lexend",sans-serif}
.bank-card .bank{position:absolute;right:16px;top:9px;text-align:right;font:500 8px/8px "Lexend",sans-serif}
.bank-card .bank small{display:block;font-size:5px;font-weight:400}
.bank-card .chip{position:absolute;left:16px;top:43px;width:16px;height:12px;border-radius:2px;background:#e6c36a}
.bank-card .number{position:absolute;left:16px;top:62px;font:400 13px "Lexend",sans-serif;word-spacing:8px;white-space:nowrap}
.bank-card .exp{position:absolute;left:16px;top:91px;font:400 5.5px "Lexend",sans-serif}
.bank-card .holder{position:absolute;left:16px;top:114px;font:400 5.5px "Lexend",sans-serif}
.bank-card .network{position:absolute;right:14px;top:108px;display:flex;align-items:center;gap:3px;font:500 6px "Lexend",sans-serif}
.bank-card .network i{width:12px;height:12px;border-radius:50%;background:#f3a33a}

/* thanks */
.close{position:absolute;right:27px;top:58px;width:16px;height:16px;border-radius:50%;background:rgba(255,255,255,.55);color:var(--olive);font:700 10px/16px "Karla",sans-serif;text-align:center}
.thanks{position:absolute;left:0;top:104px;width:231px;text-align:center;font:700 20px/24px "Karla",sans-serif;color:#fff}
.thanks-copy{position:absolute;left:16px;top:176px;width:199px;text-align:center;font:300 10px/12px "Lexend",sans-serif;color:#fff}
.sign-off{position:absolute;left:0;top:370px;width:231px;text-align:center;font:800 26px "Karla",sans-serif;color:rgba(255,255,255,.85)}

.device-view{position:absolute;top:1505px;width:208px;height:450px;border-radius:30px;overflow:hidden}
.device-view .screen{transform:scale(.9);transform-origin:0 0;border-radius:0}
</style>
</head>
<body>
<div class="stage">

<!-- ===== Row 1 ===== -->

<!-- Splash -->
<section class="screen green" style="left:52px;top:337px;height:501px">
  <div class="status"><span class="time">9:41</span><span class="island"></span>
    <svg width="36" height="9" viewBox="0 0 36 9"><rect x="0" y="6" width="2" height="3" fill="#fff"/><rect x="3" y="4" width="2" height="5" fill="#fff"/><rect x="6" y="2" width="2" height="7" fill="#fff"/><path d="M13 4a6 6 0 0 1 8 0l-1 1a4.5 4.5 0 0 0-6 0zM15 6a3 3 0 0 1 4 0l-2 2z" fill="#fff"/><rect x="25" y="1.5" width="10" height="6" rx="1.5" fill="#fff"/></svg>
  </div>
  <div class="brand" style="top:76px">Greenbowl</div>
  <div class="photo" role="img" aria-label="Fresh mixed salad in a green bowl with a pot of dressing" style="left:20px;top:150px;width:205px;height:230px;border-radius:50% 50% 40% 40%;background:radial-gradient(circle at 45% 40%,#b43f3a 0%,#7fa144 35%,#e8efe0 62%,#9fc79a 80%,rgba(166,180,127,0) 100%)"></div>
  <p class="quote" style="top:423px">"Greens produce results.<br>Dreams don't."</p>
  <span class="home-bar"></span>
</section>

<!-- Home -->
<section class="screen" style="left:300px;top:337px;height:833px">
  <div class="status"><span class="time">9:41</span><span class="island"></span>
    <svg width="36" height="9" viewBox="0 0 36 9"><rect x="0" y="6" width="2" height="3" fill="#222"/><rect x="3" y="4" width="2" height="5" fill="#222"/><rect x="6" y="2" width="2" height="7" fill="#222"/><path d="M13 4a6 6 0 0 1 8 0l-1 1a4.5 4.5 0 0 0-6 0zM15 6a3 3 0 0 1 4 0l-2 2z" fill="#222"/><rect x="25" y="1.5" width="10" height="6" rx="1.5" fill="#222"/></svg>
  </div>
  <div class="welcome">Welcome</div>
  <div class="user">Maya Torren</div>
  <div class="avatar" role="img" aria-label="Profile photo" style="left:195px;top:50px;width:22px;height:22px;background:#c9c3bb;border:1px solid #e2e2e2"></div>

  <h2 class="section-title" style="top:101px">Create Your Salad</h2>
  <p class="section-copy tiny" style="top:115px">Make your perfect salad with mixed greens, veggies, protein of choice, your favorite dressing and a sprinkle of fresh herbs.</p>
  <div class="pill" style="top:150px">Create Now</div>
  <div class="photo" role="img" aria-label="Hands tossing a fresh salad in a glass bowl" style="left:118px;top:100px;width:103px;height:66px;background:linear-gradient(135deg,#d6d8d4,#b9c79b 55%,#8d9a79)"></div>

  <h2 class="section-title" style="top:189px">Our Salad</h2>
  <p class="section-copy tiny" style="top:203px">Crafting our salads involves a medley of vibrant vegetables, a protein source, dressing and a fresh sprinkle of herbs.</p>
  <div class="pill" style="top:238px">Discover Now</div>
  <div class="photo" role="img" aria-label="Trays of colourful salad ingredients" style="left:118px;top:188px;width:103px;height:67px;background:linear-gradient(135deg,#5f7c3c,#c9532e 40%,#e5b341 65%,#3f5a2c)"></div>

  <div class="label" style="top:286px">Most Requested</div>

  <div class="rating" style="top:307px">★ 4.9</div><div class="price-tag" style="top:306px">$15</div>
  <div class="mini-card" style="top:318px;background:linear-gradient(90deg,#fff,#e7e5f4)">
    <div class="bowl" role="img" aria-label="Dream on Salad bowl" style="left:8px;background:radial-gradient(circle,#c9623e,#7d9a45 55%,#b9a58d 80%)"></div>
    <span class="kcal" style="left:110px;top:12px">311 KCAL</span>
    <span class="name" style="left:110px;top:20px;color:var(--lavender)">Dream on Salad</span>
    <span class="meta" style="left:110px;top:36px">350 g · 25 min</span>
  </div>

  <div class="rating" style="top:393px">★ 4.2</div><div class="price-tag" style="top:392px">$12</div>
  <div class="mini-card" style="top:405px;background:linear-gradient(90deg,#f4f4f4,#fff)">
    <span class="kcal" style="left:14px;top:12px">311 KCAL</span>
    <span class="name" style="left:14px;top:20px;color:var(--olive-deep)">Kale Ceasar Salad</span>
    <span class="meta" style="left:14px;top:36px">300 g · 20 min</span>
    <div class="bowl" role="img" aria-label="Kale Caesar Salad bowl" style="left:146px;background:radial-gradient(circle,#e5c24a,#8aa04a 55%,#a69479 80%)"></div>
  </div>

  <div class="rating" style="top:478px">★ 4.7</div><div class="price-tag" style="top:477px;color:#555">$20</div>
  <div class="mini-card" style="top:490px;background:linear-gradient(90deg,#cfd3dd,#fff)">
    <div class="bowl" role="img" aria-label="True Salad bowl" style="left:8px;background:radial-gradient(circle,#e9a63d,#7c9444 55%,#3b4668 85%)"></div>
    <span class="kcal" style="left:110px;top:12px">311 KCAL</span>
    <span class="name" style="left:110px;top:20px;color:var(--navy)">True Salad</span>
    <span class="meta" style="left:110px;top:36px">320 g · 15 min</span>
  </div>

  <div class="rating" style="top:564px">★ 4.2</div><div class="price-tag" style="top:563px">$15</div>
  <div class="mini-card" style="top:576px;background:linear-gradient(90deg,#e6eadc,#fff)">
    <span class="kcal" style="left:14px;top:12px">311 KCAL</span>
    <span class="name" style="left:14px;top:20px;color:#a8b58e">Halloumi Salad</span>
    <span class="meta" style="left:14px;top:36px">340 g · 20 min</span>
    <div class="bowl" role="img" aria-label="Halloumi Salad bowl" style="left:146px;background:radial-gradient(circle,#e8c46f,#6f8f3e 55%,#a69479 80%)"></div>
  </div>

  <div class="rating" style="top:650px">★ 4.2</div><div class="price-tag" style="top:649px;color:var(--peach)">$12</div>
  <div class="mini-card" style="top:662px;background:linear-gradient(90deg,#fff4e4,#fff)">
    <div class="bowl" role="img" aria-label="Korean Salad bowl" style="left:8px;background:radial-gradient(circle,#e7b347,#9aaa4d 55%,#d9b487 85%)"></div>
    <span class="kcal" style="left:110px;top:12px">311 KCAL</span>
    <span class="name" style="left:110px;top:20px;color:var(--peach)">Korean Salad</span>
    <span class="meta" style="left:110px;top:36px">330 g · 20 min</span>
  </div>

  <div class="rating" style="top:736px">★ 4.2</div><div class="price-tag" style="top:735px;color:var(--orange)">$15</div>
  <div class="mini-card" style="top:748px;background:linear-gradient(90deg,#fff,#fbe0d6)">
    <span class="kcal" style="left:14px;top:12px">311 KCAL</span>
    <span class="name" style="left:14px;top:20px;color:var(--orange)">Crab Salad</span>
    <span class="meta" style="left:14px;top:36px">360 g · 25 min</span>
    <div class="bowl" role="img" aria-label="Crab Salad bowl" style="left:146px;background:radial-gradient(circle,#e9a45d,#c9b08a 55%,#d86d4b 85%)"></div>
  </div>
</section>

<!-- Create your salad -->
<section class="screen" style="left:549px;top:337px;height:833px">
  <div class="status"><span class="time">9:41</span><span class="island"></span>
    <svg width="36" height="9" viewBox="0 0 36 9"><rect x="0" y="6" width="2" height="3" fill="#222"/><rect x="3" y="4" width="2" height="5" fill="#222"/><rect x="6" y="2" width="2" height="7" fill="#222"/><path d="M13 4a6 6 0 0 1 8 0l-1 1a4.5 4.5 0 0 0-6 0zM15 6a3 3 0 0 1 4 0l-2 2z" fill="#222"/><rect x="25" y="1.5" width="10" height="6" rx="1.5" fill="#222"/></svg>
  </div>
  <svg class="back" viewBox="0 0 16 16"><circle cx="8" cy="8" r="7.3" fill="none" stroke="#aaa" stroke-width=".8"/><path d="M9.5 4.5 6 8l3.5 3.5M6 8h5" fill="none" stroke="#aaa" stroke-width=".8"/></svg>
  <h1 class="page-title">Create Your Salad</h1>
  <div class="photo" role="img" aria-label="Green leaf salad on a white plate" style="left:48px;top:78px;width:135px;height:85px;border-radius:50%;background:radial-gradient(ellipse at 50% 40%,#7fb23a 0%,#a6cf5a 40%,#e8ece8 68%,rgba(255,255,255,0) 72%)"></div>
  <svg style="position:absolute;left:204px;top:86px" width="13" height="13" viewBox="0 0 24 24"><path d="M12 2l3 7 7 .6-5.4 4.7 1.7 7.2L12 17.8 5.7 21.5l1.7-7.2L2 9.6 9 9z" fill="#f3b43c"/></svg>
  <div class="qty" style="left:12px;top:177px"><span class="btn">+</span><span class="val">2</span><span class="btn">−</span></div>
  <div class="tiny" style="position:absolute;left:31px;top:190px">Quantity</div>
  <div class="total">Total: $8</div>
  <div class="divider-band"></div>
  <div class="tiny" style="position:absolute;left:12px;top:211px">Personalize your ingredients</div>

  <div class="step" style="top:224px"><i>1</i>Select your Greens</div>
  <div class="ing" style="left:-18px;top:268px"><div class="ing-img" role="img" aria-label="Lettuce" style="background:#6fa83b"></div><span class="ing-name">Lettuce</span><ul><li>Vegan</li><li>Gluten free</li><li>20 kcal</li></ul><span class="ing-price">$1</span></div>
  <div class="ing sel" style="left:29px;top:268px"><div class="ing-img" role="img" aria-label="Water spinach" style="background:#3f8a2c"></div><span class="ing-name">Water Spinach</span><ul><li>Vegan</li><li>Gluten free</li><li>20 kcal</li></ul><span class="ing-price">$1</span></div>
  <div class="ing" style="left:88px;top:268px"><div class="ing-img" role="img" aria-label="Butterhead lettuce" style="background:#4f9a33"></div><span class="ing-name">Butterhead Lettuce</span><ul><li>Vegan</li><li>Gluten free</li><li>20 kcal</li></ul><span class="ing-price">$1</span></div>
  <div class="ing" style="left:147px;top:268px"><div class="ing-img" role="img" aria-label="Iceberg lettuce" style="background:#5d9a44"></div><span class="ing-name">Iceberg Lettuce</span><ul><li>Vegan</li><li>Gluten free</li><li>20 kcal</li></ul><span class="ing-price">$1</span></div>
  <div class="ing" style="left:206px;top:268px"><div class="ing-img" role="img" aria-label="Spinach" style="background:#2f7a29"></div><span class="ing-name">Spinach</span><ul><li>Vegan</li><li>Gluten free</li><li>20 kcal</li></ul><span class="ing-price">$1</span></div>

  <div class="step" style="top:362px"><i>2</i>Select your Proteins</div>
  <div class="ing sel" style="left:12px;top:392px"><div class="ing-img" role="img" aria-label="Chicken breast" style="background:#e8a79a"></div><span class="ing-name">Chicken Breast</span><ul><li>Vegan</li><li>Gluten free</li><li>20 kcal</li></ul><span class="ing-price">$1</span></div>
  <div class="ing" style="left:71px;top:392px"><div class="ing-img" role="img" aria-label="Green lentils" style="background:#7fae45"></div><span class="ing-name">Lentils</span><ul><li>Vegan</li><li>Gluten free</li><li>20 kcal</li></ul><span class="ing-price">$1</span></div>
  <div class="ing" style="left:130px;top:392px"><div class="ing-img" role="img" aria-label="Tofu" style="background:#ece4cf"></div><span class="ing-name">Tofu</span><ul><li>Vegan</li><li>Gluten free</li><li>20 kcal</li></ul><span class="ing-price">$1</span></div>
  <div class="ing" style="left:189px;top:392px"><div class="ing-img" role="img" aria-label="Mushrooms" style="background:#e3dccd"></div><span class="ing-name">Mushroom</span><ul><li>Vegan</li><li>Gluten free</li><li>20 kcal</li></ul><span class="ing-price">$1</span></div>

  <div class="step" style="top:491px"><i>3</i>Select your Toppings</div>
  <div class="ing" style="left:0px;top:520px"><div class="ing-img" role="img" aria-label="Mixed nuts" style="background:#a8683a"></div><span class="ing-name">Mixed Nuts</span><ul><li>Vegan</li><li>Gluten free</li><li>20 kcal</li></ul><span class="ing-price">$1</span></div>
  <div class="ing" style="left:59px;top:520px"><div class="ing-img" role="img" aria-label="Dried fruits" style="background:#8c2f2c"></div><span class="ing-name">Dried Fruits</span><ul><li>Vegan</li><li>Gluten free</li><li>20 kcal</li></ul><span class="ing-price">$1</span></div>
  <div class="ing" style="left:118px;top:520px"><div class="ing-img" role="img" aria-label="Whole grains" style="background:#d8c59d"></div><span class="ing-name">Whole Grains</span><ul><li>Vegan</li><li>Gluten free</li><li>20 kcal</li></ul><span class="ing-price">$1</span></div>
  <div class="ing sel" style="left:177px;top:520px"><div class="ing-img" role="img" aria-label="Fresh fruits" style="background:#c7463a"></div><span class="ing-name">Fresh Fruits</span><ul><li>Vegan</li><li>Gluten free</li><li>20 kcal</li></ul><span class="ing-price">$1</span></div>

  <div class="step" style="top:622px"><i>4</i>Select your Dressings</div>
  <div class="ing" style="left:0px;top:652px"><div class="ing-img" role="img" aria-label="Honey mustard dressing" style="left:10px;width:27px;height:27px;background:#b39a22"></div><span class="ing-name">Honey Mustard</span><ul><li>Vegan</li><li>Gluten free</li><li>20 kcal</li></ul><span class="ing-price">$1</span></div>
  <div class="ing sel" style="left:59px;top:652px"><div class="ing-img" role="img" aria-label="Balsamic dressing" style="left:10px;width:27px;height:27px;background:#a88f1c"></div><span class="ing-name">Balsamic</span><ul><li>Vegan</li><li>Gluten free</li><li>20 kcal</li></ul><span class="ing-price">$1</span></div>
  <div class="ing" style="left:118px;top:652px"><div class="ing-img" role="img" aria-label="Ranch dressing" style="left:10px;width:27px;height:27px;background:#b39a22"></div><span class="ing-name">Ranch</span><ul><li>Vegan</li><li>Gluten free</li><li>20 kcal</li></ul><span class="ing-price">$1</span></div>
  <div class="ing" style="left:177px;top:652px"><div class="ing-img" role="img" aria-label="Italian dressing" style="left:10px;width:27px;height:27px;background:#b39a22"></div><span class="ing-name">Italian</span><ul><li>Vegan</li><li>Gluten free</li><li>20 kcal</li></ul><span class="ing-price">$1</span></div>

  <div class="cta" style="top:766px">Proceed to Checkout</div>
</section>

<!-- Our salad -->
<section class="screen" style="left:797px;top:337px;height:1018px">
  <div class="status"><span class="time">9:41</span><span class="island"></span>
    <svg width="36" height="9" viewBox="0 0 36 9"><rect x="0" y="6" width="2" height="3" fill="#222"/><rect x="3" y="4" width="2" height="5" fill="#222"/><rect x="6" y="2" width="2" height="7" fill="#222"/><path d="M13 4a6 6 0 0 1 8 0l-1 1a4.5 4.5 0 0 0-6 0zM15 6a3 3 0 0 1 4 0l-2 2z" fill="#222"/><rect x="25" y="1.5" width="10" height="6" rx="1.5" fill="#222"/></svg>
  </div>
  <svg class="back" viewBox="0 0 16 16"><circle cx="8" cy="8" r="7.3" fill="none" stroke="#aaa" stroke-width=".8"/><path d="M9.5 4.5 6 8l3.5 3.5M6 8h5" fill="none" stroke="#aaa" stroke-width=".8"/></svg>
  <h1 class="page-title">Our Salad</h1>

  <article class="dish" style="top:78px;background:linear-gradient(180deg,#fff,#ecebf6)">
    <div class="bowl" role="img" aria-label="Dream on Salad bowl" style="background:radial-gradient(circle,#c9623e,#7d9a45 55%,#b9a58d 80%)"></div>
    <span class="kcal">311 KCAL</span><span class="cost">$15</span>
    <h3 class="name" style="color:var(--lavender)">Dream on Salad</h3>
    <span class="meta">350 g · 25 min</span>
    <p class="desc tiny">The Dream on Salad is a vibrant mix of crisp greens, roasted beets, walnuts and creamy cheese, finished with a light house vinaigrette for a bright and balanced bite.</p>
    <div class="rev-face" role="img" aria-label="Reviewer photo" style="background:#8a7a6a"></div>
    <p class="rev">"Tastes very delicious, I like it."</p>
    <span class="stars">★★★★☆</span><span class="who">Lena</span>
    <span class="add" style="background:var(--lavender)">Add to Cart</span>
  </article>

  <article class="dish" style="top:232px;background:linear-gradient(180deg,#fff,#f1f2ea)">
    <div class="bowl" role="img" aria-label="Kale Caesar Salad bowl" style="background:radial-gradient(circle,#e5c24a,#8aa04a 55%,#a69479 80%)"></div>
    <span class="kcal">311 KCAL</span><span class="cost">$12</span>
    <h3 class="name" style="color:var(--olive-deep)">Kale Ceasar Salad</h3>
    <span class="meta">300 g · 20 min</span>
    <p class="desc tiny">The Kale Caesar Salad is a classic made with crisp kale, shaved parmesan and toasted croutons, tossed in a rich, creamy dressing that brings out every fresh flavor.</p>
    <div class="rev-face" role="img" aria-label="Reviewer photo" style="background:#4d6a8a"></div>
    <p class="rev">"The vegetables are all fresh."</p>
    <span class="stars">★★★★☆</span><span class="who">Omar</span>
    <span class="add" style="background:var(--olive)">Add to Cart</span>
  </article>

  <article class="dish" style="top:386px;background:linear-gradient(180deg,#fff,#e4e6ec)">
    <div class="bowl" role="img" aria-label="True Salad bowl" style="background:radial-gradient(circle,#e9a63d,#7c9444 55%,#3b4668 85%)"></div>
    <span class="kcal">311 KCAL</span><span class="cost" style="color:#555">$20</span>
    <h3 class="name" style="color:var(--navy)">True Salad</h3>
    <span class="meta">320 g · 15 min</span>
    <p class="desc tiny">The True Salad is a colorful medley of mixed greens, grilled chicken, sweet corn and cherry tomatoes, with a zesty lemon dressing that keeps every forkful light.</p>
    <div class="rev-face" role="img" aria-label="Reviewer photo" style="background:#6a5a4e"></div>
    <p class="rev">"A refreshing and satisfying protein-rich treat."</p>
    <span class="stars">★★★★☆</span><span class="who">Finn</span>
    <span class="add" style="background:var(--navy)">Add to Cart</span>
  </article>

  <article class="dish" style="top:540px;background:linear-gradient(180deg,#fff,#eef0e8)">
    <div class="bowl" role="img" aria-label="Halloumi Salad bowl" style="background:radial-gradient(circle,#e8c46f,#6f8f3e 55%,#a69479 80%)"></div>
    <span class="kcal">311 KCAL</span><span class="cost">$15</span>
    <h3 class="name" style="color:#a8b58e">Halloumi Salad</h3>
    <span class="meta">340 g · 20 min</span>
    <p class="desc tiny">Our Halloumi Salad pairs golden grilled halloumi with peppery rocket, cucumber and olives, drizzled with a honey lemon dressing for a warm, savory finish.</p>
    <div class="rev-face" role="img" aria-label="Reviewer photo" style="background:#3e4a5e"></div>
    <p class="rev">"The Halloumi Salad was a flavor packed delight."</p>
    <span class="stars">★★★★☆</span><span class="who">Rina</span>
    <span class="add" style="background:#b7c4d6">Add to Cart</span>
  </article>

  <article class="dish" style="top:695px;background:linear-gradient(180deg,#fff,#fdf1de)">
    <div class="bowl" role="img" aria-label="Korean Salad bowl" style="background:radial-gradient(circle,#e7b347,#9aaa4d 55%,#d9b487 85%)"></div>
    <span class="kcal">311 KCAL</span><span class="cost" style="color:var(--peach)">$12</span>
    <h3 class="name" style="color:var(--peach)">Korean Salad</h3>
    <span class="meta">330 g · 20 min</span>
    <p class="desc tiny">The Korean Salad brings crunchy cabbage, carrots and sesame together with marinated tofu and a spicy gochujang dressing for a bold, tangy twist.</p>
    <div class="rev-face" role="img" aria-label="Reviewer photo" style="background:#7a6656"></div>
    <p class="rev">"A delightful explosion of flavors with the perfect balance of freshness."</p>
    <span class="stars">★★★★☆</span><span class="who">Kenji</span>
    <span class="add" style="background:#f4c36d">Add to Cart</span>
  </article>

  <article class="dish" style="top:849px;background:linear-gradient(180deg,#fff,#fbe2d8)">
    <div class="bowl" role="img" aria-label="Crab Salad bowl" style="background:radial-gradient(circle,#e9a45d,#c9b08a 55%,#d86d4b 85%)"></div>
    <span class="kcal">311 KCAL</span><span class="cost" style="color:var(--orange)">$15</span>
    <h3 class="name" style="color:var(--orange)">Crab Salad</h3>
    <span class="meta">360 g · 25 min</span>
    <p class="desc tiny">The Crab Salad features tender crab meat, creamy avocado and crisp greens, dressed with a light citrus mayo for a fresh taste of the sea.</p>
    <div class="rev-face" role="img" aria-label="Reviewer photo" style="background:#b19a86"></div>
    <p class="rev">"The Crab Salad was a culinary masterpiece."</p>
    <span class="stars">★★★★☆</span><span class="who">Sara</span>
    <span class="add" style="background:var(--orange)">Add to Cart</span>
  </article>
</section>

<!-- Order details -->
<section class="screen" style="left:1044px;top:337px;height:711px">
  <div class="status"><span class="time">9:41</span><span class="island"></span>
    <svg width="36" height="9" viewBox="0 0 36 9"><rect x="0" y="6" width="2" height="3" fill="#222"/><rect x="3" y="4" width="2" height="5" fill="#222"/><rect x="6" y="2" width="2" height="7" fill="#222"/><path d="M13 4a6 6 0 0 1 8 0l-1 1a4.5 4.5 0 0 0-6 0zM15 6a3 3 0 0 1 4 0l-2 2z" fill="#222"/><rect x="25" y="1.5" width="10" height="6" rx="1.5" fill="#222"/></svg>
  </div>
  <svg class="back" viewBox="0 0 16 16"><circle cx="8" cy="8" r="7.3" fill="none" stroke="#aaa" stroke-width=".8"/><path d="M9.5 4.5 6 8l3.5 3.5M6 8h5" fill="none" stroke="#aaa" stroke-width=".8"/></svg>
  <h1 class="page-title">Order Details</h1>

  <div class="line-item" style="top:78px"><div class="bowl" role="img" aria-label="Dream on Salad bowl" style="background:radial-gradient(circle,#c9623e,#7d9a45 55%,#b9a58d 80%)"></div><span class="name">Dream on Salad</span><span class="each">$15 <small>/ item</small></span><div class="qty"><span class="btn">+</span><span class="val">2</span><span class="btn">−</span></div><span class="remove">×</span></div>
  <div class="line-item" style="top:152px"><div class="bowl" role="img" aria-label="Kale Caesar Salad bowl" style="background:radial-gradient(circle,#e5c24a,#8aa04a 55%,#a69479 80%)"></div><span class="name">Kale Ceasar Salad</span><span class="each">$12 <small>/ item</small></span><div class="qty"><span class="btn">+</span><span class="val">2</span><span class="btn">−</span></div><span class="remove">×</span></div>
  <div class="line-item" style="top:226px"><div class="bowl" role="img" aria-label="True Salad bowl" style="background:radial-gradient(circle,#e9a63d,#7c9444 55%,#3b4668 85%)"></div><span class="name">True Salad</span><span class="each">$12 <small>/ item</small></span><div class="qty"><span class="btn">+</span><span class="val">1</span><span class="btn">−</span></div><span class="remove">×</span></div>

  <div class="field" style="left:11px;top:298px;width:209px">Address</div>
  <div class="sum" style="top:335px"><span>Total Price</span><span>$66</span></div>
  <div class="sum" style="top:353px"><span>Discount</span><span>$0</span></div>
  <div class="sum strong" style="top:371px"><span>Payment Amount</span><span>$66</span></div>

  <div class="pay-panel">
    <div class="pay-title">Add Debit or Credit Card</div>
    <div class="bank-card">
      <span class="type">Debit.</span>
      <span class="bank">Bank Name<small>&amp; Logo</small></span>
      <span class="chip"></span>
      <span class="number">4821 0076 3310 9284</span>
      <span class="exp">12/24</span>
      <span class="holder">ALEX MORROW</span>
      <span class="network"><i></i>PAYLO</span>
    </div>
    <div class="field" style="left:11px;top:184px;width:209px">Card Number</div>
    <div class="field" style="left:11px;top:212px;width:102px">Valid Thru</div>
    <div class="field" style="left:118px;top:212px;width:102px">CVV</div>
    <div class="cta" style="left:11px;top:259px;width:209px">Checkout</div>
  </div>
</section>

<!-- Thank you -->
<section class="screen green" style="left:1291px;top:337px;height:501px">
  <div class="status"><span class="time">9:41</span><span class="island"></span>
    <svg width="36" height="9" viewBox="0 0 36 9"><rect x="0" y="6" width="2" height="3" fill="#fff"/><rect x="3" y="4" width="2" height="5" fill="#fff"/><rect x="6" y="2" width="2" height="7" fill="#fff"/><path d="M13 4a6 6 0 0 1 8 0l-1 1a4.5 4.5 0 0 0-6 0zM15 6a3 3 0 0 1 4 0l-2 2z" fill="#fff"/><rect x="25" y="1.5" width="10" height="6" rx="1.5" fill="#fff"/></svg>
  </div>
  <span class="close">×</span>
  <h1 class="thanks">Thank you<br>for choosing us!</h1>
  <p class="thanks-copy">We're delighted to have you onboard, and we hope our diverse range of salad recipes brings a burst of flavor and nutrition to your meals. Enjoy creating delicious and healthy salads with ease!</p>
  <div class="sign-off">Greenbowl</div>
  <span class="home-bar"></span>
</section>

<!-- ===== Row 2 (same flow, shorter view) ===== -->

<div class="device-view" style="left:62px">
  <section class="screen green" style="left:0;top:0;height:501px">
    <div class="status"><span class="time">9:41</span><span class="island"></span>
      <svg width="36" height="9" viewBox="0 0 36 9"><rect x="0" y="6" width="2" height="3" fill="#fff"/><rect x="3" y="4" width="2" height="5" fill="#fff"/><rect x="6" y="2" width="2" height="7" fill="#fff"/><path d="M13 4a6 6 0 0 1 8 0l-1 1a4.5 4.5 0 0 0-6 0zM15 6a3 3 0 0 1 4 0l-2 2z" fill="#fff"/><rect x="25" y="1.5" width="10" height="6" rx="1.5" fill="#fff"/></svg>
    </div>
    <div class="brand" style="top:76px">Greenbowl</div>
    <div class="photo" role="img" aria-label="Fresh mixed salad in a green bowl with a pot of dressing" style="left:20px;top:150px;width:205px;height:230px;border-radius:50% 50% 40% 40%;background:radial-gradient(circle at 45% 40%,#b43f3a 0%,#7fa144 35%,#e8efe0 62%,#9fc79a 80%,rgba(166,180,127,0) 100%)"></div>
    <p class="quote" style="top:423px">"Greens produce results.<br>Dreams don't."</p>
    <span class="home-bar"></span>
  </section>
</div>

<div class="device-view" style="left:309px">
  <section class="screen" style="left:0;top:0;height:501px">
    <div class="status"><span class="time">9:41</span><span class="island"></span>
      <svg width="36" height="9" viewBox="0 0 36 9"><rect x="0" y="6" width="2" height="3" fill="#222"/><rect x="3" y="4" width="2" height="5" fill="#222"/><rect x="6" y="2" width="2" height="7" fill="#222"/><path d="M13 4a6 6 0 0 1 8 0l-1 1a4.5 4.5 0 0 0-6 0zM15 6a3 3 0 0 1 4 0l-2 2z" fill="#222"/><rect x="25" y="1.5" width="10" height="6" rx="1.5" fill="#222"/></svg>
    </div>
    <div class="welcome">Welcome</div>
    <div class="user">Maya Torren</div>
    <div class="avatar" role="img" aria-label="Profile photo" style="left:195px;top:50px;width:22px;height:22px;background:#c9c3bb"></div>
    <h2 class="section-title" style="top:101px">Create Your Salad</h2>
    <p class="section-copy tiny" style="top:115px">Make your perfect salad with mixed greens, veggies, protein of choice, your favorite dressing and a sprinkle of fresh herbs.</p>
    <div class="pill" style="top:150px">Create Now</div>
    <div class="photo" role="img" aria-label="Hands tossing a fresh salad in a glass bowl" style="left:118px;top:100px;width:103px;height:66px;background:linear-gradient(135deg,#d6d8d4,#b9c79b 55%,#8d9a79)"></div>
    <h2 class="section-title" style="top:189px">Our Salad</h2>
    <p class="section-copy tiny" style="top:203px">Crafting our salads involves a medley of vibrant vegetables, a protein source, dressing and a fresh sprinkle of herbs.</p>
    <div class="pill" style="top:238px">Discover Now</div>
    <div class="photo" role="img" aria-label="Trays of colourful salad ingredients" style="left:118px;top:188px;width:103px;height:67px;background:linear-gradient(135deg,#5f7c3c,#c9532e 40%,#e5b341 65%,#3f5a2c)"></div>
    <div class="label" style="top:286px">Most Requested</div>
    <div class="rating" style="top:307px">★ 4.9</div><div class="price-tag" style="top:306px">$15</div>
    <div class="mini-card" style="top:318px;background:linear-gradient(90deg,#fff,#e7e5f4)">
      <div class="bowl" role="img" aria-label="Dream on Salad bowl" style="left:8px;background:radial-gradient(circle,#c9623e,#7d9a45 55%,#b9a58d 80%)"></div>
      <span class="kcal" style="left:110px;top:12px">311 KCAL</span>
      <span class="name" style="left:110px;top:20px;color:var(--lavender)">Dream on Salad</span>
      <span class="meta" style="left:110px;top:36px">350 g · 25 min</span>
    </div>
    <div class="rating" style="top:393px">★ 4.2</div><div class="price-tag" style="top:392px">$12</div>
    <div class="mini-card" style="top:405px;background:linear-gradient(90deg,#f4f4f4,#fff)">
      <span class="kcal" style="left:14px;top:12px">311 KCAL</span>
      <span class="name" style="left:14px;top:20px;color:var(--olive-deep)">Kale Ceasar Salad</span>
      <span class="meta" style="left:14px;top:36px">300 g · 20 min</span>
      <div class="bowl" role="img" aria-label="Kale Caesar Salad bowl" style="left:146px;background:radial-gradient(circle,#e5c24a,#8aa04a 55%,#a69479 80%)"></div>
    </div>
    <div class="rating" style="top:478px">★ 4.2</div><div class="price-tag" style="top:477px;color:#555">$20</div>
    <span class="home-bar"></span>
  </section>
</div>

<div class="device-view" style="left:558px">
  <section class="screen" style="left:0;top:0;height:501px">
    <div class="status"><span class="time">9:41</span><span class="island"></span>
      <svg width="36" height="9" viewBox="0 0 36 9"><rect x="0" y="6" width="2" height="3" fill="#222"/><rect x="3" y="4" width="2" height="5" fill="#222"/><rect x="6" y="2" width="2" height="7" fill="#222"/><path d="M13 4a6 6 0 0 1 8 0l-1 1a4.5 4.5 0 0 0-6 0zM15 6a3 3 0 0 1 4 0l-2 2z" fill="#222"/><rect x="25" y="1.5" width="10" height="6" rx="1.5" fill="#222"/></svg>
    </div>
    <svg class="back" viewBox="0 0 16 16"><circle cx="8" cy="8" r="7.3" fill="none" stroke="#aaa" stroke-width=".8"/><path d="M9.5 4.5 6 8l3.5 3.5M6 8h5" fill="none" stroke="#aaa" stroke-width=".8"/></svg>
    <h1 class="page-title">Create Your Salad</h1>
    <div class="photo" role="img" aria-label="Green leaf salad on a white plate" style="left:48px;top:78px;width:135px;height:85px;border-radius:50%;background:radial-gradient(ellipse at 50% 40%,#7fb23a 0%,#a6cf5a 40%,#e8ece8 68%,rgba(255,255,255,0) 72%)"></div>
    <svg style="position:absolute;left:204px;top:86px" width="13" height="13" viewBox="0 0 24 24"><path d="M12 2l3 7 7 .6-5.4 4.7 1.7 7.2L12 17.8 5.7 21.5l1.7-7.2L2 9.6 9 9z" fill="#f3b43c"/></svg>
    <div class="qty" style="left:12px;top:177px"><span class="btn">+</span><span class="val">2</span><span class="btn">−</span></div>
    <div class="tiny" style="position:absolute;left:31px;top:190px">Quantity</div>
    <div class="total">Total: $8</div>
    <div class="divider-band"></div>
    <div class="tiny" style="position:absolute;left:12px;top:211px">Personalize your ingredients</div>
    <div class="step" style="top:224px"><i>1</i>Select your Greens</div>
    <div class="ing" style="left:-18px;top:268px"><div class="ing-img" role="img" aria-label="Lettuce" style="background:#6fa83b"></div><span class="ing-name">Lettuce</span><ul><li>Vegan</li><li>Gluten free</li><li>20 kcal</li></ul><span class="ing-price">$1</span></div>
    <div class="ing sel" style="left:29px;top:268px"><div class="ing-img" role="img" aria-label="Water spinach" style="background:#3f8a2c"></div><span class="ing-name">Water Spinach</span><ul><li>Vegan</li><li>Gluten free</li><li>20 kcal</li></ul><span class="ing-price">$1</span></div>
    <div class="ing" style="left:88px;top:268px"><div class="ing-img" role="img" aria-label="Butterhead lettuce" style="background:#4f9a33"></div><span class="ing-name">Butterhead Lettuce</span><ul><li>Vegan</li><li>Gluten free</li><li>20 kcal</li></ul><span class="ing-price">$1</span></div>
    <div class="ing" style="left:147px;top:268px"><div class="ing-img" role="img" aria-label="Iceberg lettuce" style="background:#5d9a44"></div><span class="ing-name">Iceberg Lettuce</span><ul><li>Vegan</li><li>Gluten free</li><li>20 kcal</li></ul><span class="ing-price">$1</span></div>
    <div class="ing" style="left:206px;top:268px"><div class="ing-img" role="img" aria-label="Spinach" style="background:#2f7a29"></div><span class="ing-name">Spinach</span><ul><li>Vegan</li><li>Gluten free</li><li>20 kcal</li></ul><span class="ing-price">$1</span></div>
    <div class="step" style="top:362px"><i>2</i>Select your Proteins</div>
    <div class="ing sel" style="left:12px;top:392px"><div class="ing-img" role="img" aria-label="Chicken breast" style="background:#e8a79a"></div><span class="ing-name">Chicken Breast</span><ul><li>Vegan</li><li>Gluten free</li><li>20 kcal</li></ul><span class="ing-price">$1</span></div>
    <div class="ing" style="left:71px;top:392px"><div class="ing-img" role="img" aria-label="Green lentils" style="background:#7fae45"></div><span class="ing-name">Lentils</span><ul><li>Vegan</li><li>Gluten free</li><li>20 kcal</li></ul><span class="ing-price">$1</span></div>
    <div class="ing" style="left:130px;top:392px"><div class="ing-img" role="img" aria-label="Tofu" style="background:#ece4cf"></div><span class="ing-name">Tofu</span><ul><li>Vegan</li><li>Gluten free</li><li>20 kcal</li></ul><span class="ing-price">$1</span></div>
    <div class="ing" style="left:189px;top:392px"><div class="ing-img" role="img" aria-label="Mushrooms" style="background:#e3dccd"></div><span class="ing-name">Mushroom</span><ul><li>Vegan</li><li>Gluten free</li><li>20 kcal</li></ul><span class="ing-price">$1</span></div>
    <div class="step" style="top:491px"><i>3</i>Select your Toppings</div>
  </section>
</div>

<div class="device-view" style="left:806px">
  <section class="screen" style="left:0;top:0;height:501px">
    <div class="status"><span class="time">9:41</span><span class="island"></span>
      <svg width="36" height="9" viewBox="0 0 36 9"><rect x="0" y="6" width="2" height="3" fill="#222"/><rect x="3" y="4" width="2" height="5" fill="#222"/><rect x="6" y="2" width="2" height="7" fill="#222"/><path d="M13 4a6 6 0 0 1 8 0l-1 1a4.5 4.5 0 0 0-6 0zM15 6a3 3 0 0 1 4 0l-2 2z" fill="#222"/><rect x="25" y="1.5" width="10" height="6" rx="1.5" fill="#222"/></svg>
    </div>
    <svg class="back" viewBox="0 0 16 16"><circle cx="8" cy="8" r="7.3" fill="none" stroke="#aaa" stroke-width=".8"/><path d="M9.5 4.5 6 8l3.5 3.5M6 8h5" fill="none" stroke="#aaa" stroke-width=".8"/></svg>
    <h1 class="page-title">Our Salad</h1>
    <article class="dish" style="top:78px;background:linear-gradient(180deg,#fff,#ecebf6)">
      <div class="bowl" role="img" aria-label="Dream on Salad bowl" style="background:radial-gradient(circle,#c9623e,#7d9a45 55%,#b9a58d 80%)"></div>
      <span class="kcal">311 KCAL</span><span class="cost">$15</span>
      <h3 class="name" style="color:var(--lavender)">Dream on Salad</h3>
      <span class="meta">350 g · 25 min</span>
      <p class="desc tiny">The Dream on Salad is a vibrant mix of crisp greens, roasted beets, walnuts and creamy cheese, finished with a light house vinaigrette for a bright and balanced bite.</p>
      <div class="rev-face" role="img" aria-label="Reviewer photo" style="background:#8a7a6a"></div>
      <p class="rev">"Tastes very delicious, I like it."</p>
      <span class="stars">★★★★☆</span><span class="who">Lena</span>
      <span class="add" style="background:var(--lavender)">Add to Cart</span>
    </article>
    <article class="dish" style="top:232px;background:linear-gradient(180deg,#fff,#f1f2ea)">
      <div class="bowl" role="img" aria-label="Kale Caesar Salad bowl" style="background:radial-gradient(circle,#e5c24a,#8aa04a 55%,#a69479 80%)"></div>
      <span class="kcal">311 KCAL</span><span class="cost">$12</span>
      <h3 class="name" style="color:var(--olive-deep)">Kale Ceasar Salad</h3>
      <span class="meta">300 g · 20 min</span>
      <p class="desc tiny">The Kale Caesar Salad is a classic made with crisp kale, shaved parmesan and toasted croutons, tossed in a rich, creamy dressing that brings out every fresh flavor.</p>
      <div class="rev-face" role="img" aria-label="Reviewer photo" style="background:#4d6a8a"></div>
      <p class="rev">"The vegetables are all fresh."</p>
      <span class="stars">★★★★☆</span><span class="who">Omar</span>
      <span class="add" style="background:var(--olive)">Add to Cart</span>
    </article>
    <article class="dish" style="top:386px;background:linear-gradient(180deg,#fff,#e4e6ec)">
      <div class="bowl" role="img" aria-label="True Salad bowl" style="background:radial-gradient(circle,#e9a63d,#7c9444 55%,#3b4668 85%)"></div>
      <span class="kcal">311 KCAL</span><span class="cost" style="color:#555">$20</span>
      <h3 class="name" style="color:var(--navy)">True Salad</h3>
      <span class="meta">320 g · 15 min</span>
      <p class="desc tiny">The True Salad is a colorful medley of mixed greens, grilled chicken, sweet corn and cherry tomatoes, with a zesty lemon dressing that keeps every forkful light.</p>
      <div class="rev-face" role="img" aria-label="Reviewer photo" style="background:#6a5a4e"></div>
      <p class="rev">"A refreshing and satisfying protein-rich treat."</p>
      <span class="stars">★★★★☆</span><span class="who">Finn</span>
      <span class="add" style="background:var(--navy)">Add to Cart</span>
    </article>
  </section>
</div>

<div class="device-view" style="left:1054px">
  <section class="screen" style="left:0;top:0;height:501px">
    <div class="status"><span class="time">9:41</span><span class="island"></span>
      <svg width="36" height="9" viewBox="0 0 36 9"><rect x="0" y="6" width="2" height="3" fill="#222"/><rect x="3" y="4" width="2" height="5" fill="#222"/><rect x="6" y="2" width="2" height="7" fill="#222"/><path d="M13 4a6 6 0 0 1 8 0l-1 1a4.5 4.5 0 0 0-6 0zM15 6a3 3 0 0 1 4 0l-2 2z" fill="#222"/><rect x="25" y="1.5" width="10" height="6" rx="1.5" fill="#222"/></svg>
    </div>
    <svg class="back" viewBox="0 0 16 16"><circle cx="8" cy="8" r="7.3" fill="none" stroke="#aaa" stroke-width=".8"/><path d="M9.5 4.5 6 8l3.5 3.5M6 8h5" fill="none" stroke="#aaa" stroke-width=".8"/></svg>
    <h1 class="page-title">Order Details</h1>
    <div class="line-item" style="top:78px"><div class="bowl" role="img" aria-label="Dream on Salad bowl" style="background:radial-gradient(circle,#c9623e,#7d9a45 55%,#b9a58d 80%)"></div><span class="name">Dream on Salad</span><span class="each">$15 <small>/ item</small></span><div class="qty"><span class="btn">+</span><span class="val">2</span><span class="btn">−</span></div><span class="remove">×</span></div>
    <div class="line-item" style="top:152px"><div class="bowl" role="img" aria-label="Kale Caesar Salad bowl" style="background:radial-gradient(circle,#e5c24a,#8aa04a 55%,#a69479 80%)"></div><span class="name">Kale Ceasar Salad</span><span class="each">$12 <small>/ item</small></span><div class="qty"><span class="btn">+</span><span class="val">2</span><span class="btn">−</span></div><span class="remove">×</span></div>
    <div class="line-item" style="top:226px"><div class="bowl" role="img" aria-label="True Salad bowl" style="background:radial-gradient(circle,#e9a63d,#7c9444 55%,#3b4668 85%)"></div><span class="name">True Salad</span><span class="each">$12 <small>/ item</small></span><div class="qty"><span class="btn">+</span><span class="val">1</span><span class="btn">−</span></div><span class="remove">×</span></div>
    <div class="field" style="left:11px;top:298px;width:209px">Address</div>
    <div class="sum" style="top:335px"><span>Total Price</span><span>$66</span></div>
    <div class="sum" style="top:353px"><span>Discount</span><span>$0</span></div>
    <div class="sum strong" style="top:371px"><span>Payment Amount</span><span>$66</span></div>
    <div class="pay-panel">
      <div class="pay-title">Add Debit or Credit Card</div>
      <div class="bank-card">
        <span class="type">Debit.</span>
        <span class="bank">Bank Name<small>&amp; Logo</small></span>
        <span class="chip"></span>
      </div>
    </div>
  </section>
</div>

<div class="device-view" style="left:1302px">
  <section class="screen green" style="left:0;top:0;height:501px">
    <div class="status"><span class="time">9:41</span><span class="island"></span>
      <svg width="36" height="9" viewBox="0 0 36 9"><rect x="0" y="6" width="2" height="3" fill="#fff"/><rect x="3" y="4" width="2" height="5" fill="#fff"/><rect x="6" y="2" width="2" height="7" fill="#fff"/><path d="M13 4a6 6 0 0 1 8 0l-1 1a4.5 4.5 0 0 0-6 0zM15 6a3 3 0 0 1 4 0l-2 2z" fill="#fff"/><rect x="25" y="1.5" width="10" height="6" rx="1.5" fill="#fff"/></svg>
    </div>
    <span class="close">×</span>
    <h1 class="thanks">Thank you<br>for choosing us!</h1>
    <p class="thanks-copy">We're delighted to have you onboard, and we hope our diverse range of salad recipes brings a burst of flavor and nutrition to your meals. Enjoy creating delicious and healthy salads with ease!</p>
    <div class="sign-off">Greenbowl</div>
    <span class="home-bar"></span>
  </section>
</div>

</div>
</body>
</html>
```